Remake homepage in our website

To redesign the homepage of Datavane's website, highlighting its key solutions: Ferrolith, Joltmesh, and BXN Relay. The goal is to communicate Datavane's value proposition effectively, attract potential clients, and provide an intuitive navigation experience.
Target Audience
Primary Audience: Decision-makers in the industrial sector, including plant managers, automation engineers, and IT managers.
Secondary Audience: Current clients and stakeholders looking to explore new solutions.
Key Messages
Datavane is a leader in connectivity, cybersecurity, and industrial data management solutions.
Ferrolith, Joltmesh, and BXN Relay are innovative tools designed to optimize industrial operations.
Datavane offers personalized support and over two decades of expertise.
Deliverables
Homepage Design:
Hero section with a strong headline, supportive subhead, and prominent CTAs.
Clear presentation of Ferrolith, Joltmesh, and BXN Relay with brief descriptions and links to more details.
Visual elements (e.g., icons, images, videos) that align with the brand's identity.
Sections showcasing Datavane's experience and client testimonials.
Content Development:
Copywriting for each section of the homepage.
Visual assets (e.g., illustrations, photos, and short videos) for product highlights and brand storytelling.
Requirements
Modern and professional design aligned with Datavane's branding.
Intuitive navigation that guides users to key sections and CTAs.
Integration with the existing CMS or website platform.
Testing to ensure responsiveness and functionality across devices.

```html
<!DOCTYPE html>
<html lang="en">
<head>
<meta charset="utf-8">
<title>Datavane – Connectivity and Industrial Efficiency</title>
<link href="https://fonts.googleapis.com/css2?family=Poppins:wght@300;400;500;600;700;800&display=swap" rel="stylesheet">
<style>
:root{
  --blue:#0a78c2;
  --blue-bright:#1a8fd9;
  --ink:#111827;
  --night:#04080f;
  --navy:#07152e;
  --grey:#9aa1ab;
  --grey-text:#8a8f96;
  --line:#d7dbe0;
  --white:#ffffff;
  --star:#f4a21d;
}
*{box-sizing:border-box;margin:0;padding:0}
html,body{width:1200px;height:3645px;overflow:hidden}
body{font-family:'Poppins',sans-serif;background:var(--white);color:var(--ink);position:relative}
.abs{position:absolute}
svg.shape{position:absolute;left:0;display:block}

/* header + hero */
.hero-bg{top:0;width:1200px;height:700px}
.hero-art{left:600px;top:110px;width:600px;height:420px;
  background:radial-gradient(ellipse at 55% 35%,#1f8fe0 0%,#0b3d72 28%,rgba(4,8,15,0) 62%);}
.brand{font-weight:500;font-size:26px;color:var(--white);display:flex;align-items:center;gap:10px;letter-spacing:.5px}
.brand .mark{width:10px;height:10px;background:var(--blue-bright)}
.site-brand{left:105px;top:32px}
.nav{top:43px;left:410px;display:flex;gap:34px;font-size:11px;font-weight:600;color:#dfe4ea;text-transform:uppercase}
.nav .home{width:14px;height:14px;fill:var(--blue-bright)}
.btn{background:var(--blue);color:var(--white);font-weight:600;text-transform:uppercase;font-size:11px;display:flex;align-items:center;justify-content:center}
.nav-cta{left:975px;top:32px;width:119px;height:38px}
.eyebrow{left:89px;top:150px;font-size:11px;font-weight:700;color:var(--white)}
.hero-title{left:89px;top:174px;font-size:41px;line-height:45px;font-weight:800;color:var(--white);text-transform:uppercase}
.hero-title em{font-style:normal;color:var(--blue-bright)}
.hero-sub{left:89px;top:318px;font-size:14px;line-height:20px;color:#e7ebf0;width:440px}
.hero-cta{left:89px;top:379px;width:159px;height:38px}
.slides{left:48px;top:198px;font-size:11px;font-weight:700;color:var(--white);line-height:27px}
.slides .on{color:var(--blue-bright)}
.slides .arr{color:var(--blue-bright);font-weight:400}

/* solutions */
.section-title{width:1200px;text-align:center;font-size:34px;font-weight:800;text-transform:uppercase;color:#a9aeb5;letter-spacing:.3px}
.section-title em{font-style:normal;color:var(--blue)}
.section-sub{width:1200px;text-align:center;font-size:13px;line-height:20px;color:var(--grey-text)}
.card{top:887px;width:263px;height:333px;background:var(--white);box-shadow:0 6px 24px rgba(20,40,80,.09)}
.card .media{height:166px}
.card h3{margin:34px 13px 6px;font-size:20px;font-weight:700;color:var(--blue);text-transform:uppercase}
.card p{margin:0 13px;font-size:13px;line-height:19px;color:var(--grey-text)}
.m1{background:linear-gradient(135deg,#d7dde3,#7ea3b8 55%,#3c5a6a)}
.m2{background:linear-gradient(135deg,#2b5a8f,#5a86b5 55%,#c24a2a)}
.m3{background:linear-gradient(160deg,#2a6ea0,#13324f 60%,#0b1a2b)}

/* why */
.why-art{left:150px;top:1400px;width:430px;height:387px;
  background:radial-gradient(ellipse at 50% 40%,#8fd0ff 0%,#3b78c4 30%,rgba(8,22,50,0) 65%);}
.why-title{left:709px;top:1535px;font-size:33px;line-height:45px;font-weight:800;color:var(--white);text-transform:uppercase}
.ticks{left:709px;top:1640px;list-style:none;font-size:14px;line-height:20px;color:var(--white)}
.ticks li{display:flex;align-items:center;gap:8px}
.ticks svg{width:13px;height:13px}

/* testimonials */
.quote{width:406px;height:234px;border:1px solid var(--line);background:var(--white);padding:32px 35px 0}
.quote .who{display:flex;align-items:center;gap:12px;font-size:14px;font-weight:700;text-transform:uppercase;white-space:nowrap}
.quote .avatar{width:52px;height:52px;border-radius:50%;flex:none}
.quote p{margin-top:22px;font-size:13px;line-height:19px;color:var(--grey-text)}
.stars{margin-top:8px;display:flex;gap:2px}
.stars svg{width:16px;height:16px;fill:var(--star)}
.a1{background:#c9706a}.a2{background:#8a5a4a}.a3{background:#9c7a62}.a4{background:#c89b84}.a5{background:#8c4f79}
.slider-btn{width:40px;height:40px;border-radius:50%;color:var(--white);display:flex;align-items:center;justify-content:center;font-size:16px}
.prev{left:15px;top:2117px;background:var(--blue)}
.next{left:1112px;top:2366px;background:#b5b9bf}

/* contact */
.contact-title{left:133px;top:2832px;font-size:35px;line-height:46px;font-weight:800;color:var(--white);text-transform:uppercase}
.contact-lead{left:133px;top:2937px;font-size:14px;color:var(--white)}
.reach{left:133px;display:flex;align-items:center;gap:12px;color:var(--white)}
.reach .ico{width:43px;height:43px;border-radius:50%;background:var(--blue);display:flex;align-items:center;justify-content:center}
.reach .ico svg{width:20px;height:20px;fill:none;stroke:#fff;stroke-width:2}
.reach small{display:block;font-size:10px;font-weight:600}
.reach b{font-size:15px;font-weight:700}
.form-label{left:611px;top:2817px;font-size:13px;font-weight:700;color:var(--white);text-transform:uppercase}
.field{background:var(--white);border:1px solid #cfd5dc;font-size:10px;color:#6f757d;padding:12px 18px}
.submit{left:611px;top:3127px;width:160px;height:39px}

/* footer */
.foot-brand{left:120px;top:3393px;color:var(--blue);font-size:28px}
.socials{left:130px;top:3449px;display:flex;gap:10px}
.socials span{width:26px;height:26px;border-radius:50%;background:var(--blue)}
.foot-h{top:3311px;font-size:26px;font-weight:800;text-transform:uppercase;color:var(--ink)}
.foot-list{list-style:none;font-size:14px;line-height:18px;color:#6f757d}
.foot-list li{margin-bottom:9px}
.foot-contact li{display:flex;gap:10px;align-items:flex-start}
.foot-contact svg{width:13px;height:13px;flex:none;margin-top:2px;fill:var(--blue)}
.news{left:838px;top:3366px;width:271px;height:45px;border:1px solid #bfc5cc;display:flex;align-items:center;justify-content:space-between;padding:0 20px;font-size:13px;color:#6f757d}
.news svg{width:16px;height:16px;fill:var(--blue)}
.rule{left:133px;top:3583px;width:933px;height:1px;background:#e2e5e9}
.copy{top:3606px;width:1200px;text-align:center;font-size:13px;color:#6f757d}
.chat-fab{left:1126px;top:3572px;width:42px;height:38px}
</style>
</head>
<body>

<!-- hero -->
<svg class="shape hero-bg" width="1200" height="700" viewBox="0 0 1200 700">
  <polygon points="0,0 1200,0 1200,535 872,665 0,526" fill="#04080f"/>
  <polygon points="0,526 872,665 1200,535 1200,545 872,693 0,540" fill="#0a78c2"/>
  <polyline points="0,540 872,693 1200,545" fill="none" stroke="#9aa1ab" stroke-width="1"/>
</svg>
<div class="abs hero-art" role="img" aria-label="Glowing digital brain rising above a circuit board"></div>

<div class="abs brand site-brand"><span class="mark"></span>Datavane</div>
<nav class="abs nav">
  <svg class="home" viewBox="0 0 16 16"><path d="M8 1 1 8h2v7h4v-5h2v5h4V8h2z"/></svg>
  <span>Solutions</span><span>Benefits of choosing Datavane</span><span>Testimonials</span>
</nav>
<div class="abs btn nav-cta">Contact</div>

<div class="abs slides">
  <div class="arr">↑</div><div class="on">01</div><div>02</div><div>03</div><div>04</div><div>05</div><div class="arr">↓</div>
</div>
<div class="abs eyebrow">WELCOME TO DATAVANE</div>
<h1 class="abs hero-title">Empowering<br><em>Connectivity</em> and<br>Industrial <em>Efficiency</em></h1>
<p class="abs hero-sub">Leading solutions in cybersecurity, connectivity, and data management for Industry 4.0</p>
<div class="abs btn hero-cta">Explore Joltmesh</div>

<!-- solutions -->
<h2 class="abs section-title" style="top:782px"><em>Solutions</em> that <em>transform</em> your plant</h2>
<p class="abs section-sub" style="top:832px">A brief description of each solution with a link to learn more</p>

<article class="abs card" style="left:187px">
  <div class="media m1" role="img" aria-label="Monitor showing plant management software"></div>
  <h3>Ferrolith</h3>
  <p>Comprehensive automation management and data backup for uninterrupted industrial operations.</p>
</article>
<article class="abs card" style="left:470px">
  <div class="media m2" role="img" aria-label="Engineer at an industrial site with connectivity icons"></div>
  <h3>Joltmesh</h3>
  <p>Reliable connectivity between industrial systems and devices.</p>
</article>
<article class="abs card" style="left:750px">
  <div class="media m3" role="img" aria-label="City skyline at dusk with network icons"></div>
  <h3>BXN Relay</h3>
  <p>Advanced integration to optimize plant communication.</p>
</article>

<!-- why -->
<svg class="shape" style="top:1310px" width="1200" height="480" viewBox="0 1310 1200 480">
  <polygon points="0,1479 320,1323 1200,1486 1200,1787 0,1787" fill="#07152e"/>
  <polygon points="0,1468 320,1313 1200,1476 1200,1486 320,1323 0,1479" fill="#0a78c2"/>
  <polygon points="320,1323 1200,1486 1200,1787 700,1787" fill="#04080f" opacity=".55"/>
</svg>
<div class="abs why-art" role="img" aria-label="Hand holding a tablet with a holographic cloud above a city"></div>
<h2 class="abs why-title">Why Datavane is<br>your strategic ally</h2>
<ul class="abs ticks">
  <li><svg viewBox="0 0 14 14"><circle cx="7" cy="7" r="7" fill="#1a8fd9"/><path d="M4 7.2 6.2 9.3 10 5" stroke="#fff" stroke-width="1.6" fill="none"/></svg>Over 20 years of experience in industrial solutions.</li>
  <li><svg viewBox="0 0 14 14"><circle cx="7" cy="7" r="7" fill="#1a8fd9"/><path d="M4 7.2 6.2 9.3 10 5" stroke="#fff" stroke-width="1.6" fill="none"/></svg>Team of experts in connectivity and automation.</li>
  <li><svg viewBox="0 0 14 14"><circle cx="7" cy="7" r="7" fill="#1a8fd9"/><path d="M4 7.2 6.2 9.3 10 5" stroke="#fff" stroke-width="1.6" fill="none"/></svg>Personalized technical support</li>
</ul>

<!-- testimonials -->
<h2 class="abs section-title" style="top:1884px">Success <em>stories</em></h2>
<p class="abs section-sub" style="top:1936px">Client testimonials highlighting the impact of Ferrolith,<br>Joltmesh, and BXN Relay on their operations.</p>

<div class="abs slider-btn prev">‹</div>

<div class="abs quote" style="left:74px;top:2014px">
  <div class="who"><span class="avatar a1" role="img" aria-label="Client portrait"></span>Marcus United Kingdom</div>
  <p>I've been selling successfully on our marketplace for almost 5 years. The wholesale list upload feature has saved me HOURS every day and is now essential for my business!</p>
  <div class="stars"><svg viewBox="0 0 20 20"><path d="m10 1 2.8 6 6.2.6-4.7 4.2 1.4 6.2L10 14.8 4.3 18l1.4-6.2L1 7.6 7.2 7z"/></svg><svg viewBox="0 0 20 20"><path d="m10 1 2.8 6 6.2.6-4.7 4.2 1.4 6.2L10 14.8 4.3 18l1.4-6.2L1 7.6 7.2 7z"/></svg><svg viewBox="0 0 20 20"><path d="m10 1 2.8 6 6.2.6-4.7 4.2 1.4 6.2L10 14.8 4.3 18l1.4-6.2L1 7.6 7.2 7z"/></svg><svg viewBox="0 0 20 20"><path d="m10 1 2.8 6 6.2.6-4.7 4.2 1.4 6.2L10 14.8 4.3 18l1.4-6.2L1 7.6 7.2 7z"/></svg><svg viewBox="0 0 20 20"><path d="m10 1 2.8 6 6.2.6-4.7 4.2 1.4 6.2L10 14.8 4.3 18l1.4-6.2L1 7.6 7.2 7z"/></svg></div>
</div>
<div class="abs quote" style="left:525px;top:2014px">
  <div class="who"><span class="avatar a2" role="img" aria-label="Client portrait"></span>Renata United States</div>
  <p>Ferrolith has allowed me to add another revenue stream to my business with very little effort. I personally love the sales history charts - very useful.</p>
  <div class="stars"><svg viewBox="0 0 20 20"><path d="m10 1 2.8 6 6.2.6-4.7 4.2 1.4 6.2L10 14.8 4.3 18l1.4-6.2L1 7.6 7.2 7z"/></svg><svg viewBox="0 0 20 20"><path d="m10 1 2.8 6 6.2.6-4.7 4.2 1.4 6.2L10 14.8 4.3 18l1.4-6.2L1 7.6 7.2 7z"/></svg><svg viewBox="0 0 20 20"><path d="m10 1 2.8 6 6.2.6-4.7 4.2 1.4 6.2L10 14.8 4.3 18l1.4-6.2L1 7.6 7.2 7z"/></svg><svg viewBox="0 0 20 20"><path d="m10 1 2.8 6 6.2.6-4.7 4.2 1.4 6.2L10 14.8 4.3 18l1.4-6.2L1 7.6 7.2 7z"/></svg><svg viewBox="0 0 20 20"><path d="m10 1 2.8 6 6.2.6-4.7 4.2 1.4 6.2L10 14.8 4.3 18l1.4-6.2L1 7.6 7.2 7z"/></svg></div>
</div>
<div class="abs quote" style="left:978px;top:2014px">
  <div class="who"><span class="avatar a3" role="img" aria-label="Client portrait"></span>Pieter South Africa</div>
  <p>Using Joltmesh has provided me a full time income. I buy and run my business from South Africa and the support team are really helpful.</p>
  <div class="stars"><svg viewBox="0 0 20 20"><path d="m10 1 2.8 6 6.2.6-4.7 4.2 1.4 6.2L10 14.8 4.3 18l1.4-6.2L1 7.6 7.2 7z"/></svg><svg viewBox="0 0 20 20"><path d="m10 1 2.8 6 6.2.6-4.7 4.2 1.4 6.2L10 14.8 4.3 18l1.4-6.2L1 7.6 7.2 7z"/></svg><svg viewBox="0 0 20 20"><path d="m10 1 2.8 6 6.2.6-4.7 4.2 1.4 6.2L10 14.8 4.3 18l1.4-6.2L1 7.6 7.2 7z"/></svg><svg viewBox="0 0 20 20"><path d="m10 1 2.8 6 6.2.6-4.7 4.2 1.4 6.2L10 14.8 4.3 18l1.4-6.2L1 7.6 7.2 7z"/></svg><svg viewBox="0 0 20 20"><path d="m10 1 2.8 6 6.2.6-4.7 4.2 1.4 6.2L10 14.8 4.3 18l1.4-6.2L1 7.6 7.2 7z"/></svg></div>
</div>

<div class="abs quote" style="left:-216px;top:2271px">
  <div class="who"><span class="avatar a1" role="img" aria-label="Client portrait"></span>Marcus United Kingdom</div>
  <p>I've been selling successfully on our marketplace for almost 5 years. The wholesale list upload feature has saved me HOURS every day and is now essential.</p>
</div>
<div class="abs quote" style="left:235px;top:2271px">
  <div class="who"><span class="avatar a4" role="img" aria-label="Client portrait"></span>Clara United States</div>
  <p>Ferrolith is the first thing I open in the morning, and the last thing I close at night. Simply awesome software that pays for itself! Keep it up guys!</p>
  <div class="stars"><svg viewBox="0 0 20 20"><path d="m10 1 2.8 6 6.2.6-4.7 4.2 1.4 6.2L10 14.8 4.3 18l1.4-6.2L1 7.6 7.2 7z"/></svg><svg viewBox="0 0 20 20"><path d="m10 1 2.8 6 6.2.6-4.7 4.2 1.4 6.2L10 14.8 4.3 18l1.4-6.2L1 7.6 7.2 7z"/></svg><svg viewBox="0 0 20 20"><path d="m10 1 2.8 6 6.2.6-4.7 4.2 1.4 6.2L10 14.8 4.3 18l1.4-6.2L1 7.6 7.2 7z"/></svg><svg viewBox="0 0 20 20"><path d="m10 1 2.8 6 6.2.6-4.7 4.2 1.4 6.2L10 14.8 4.3 18l1.4-6.2L1 7.6 7.2 7z"/></svg><svg viewBox="0 0 20 20"><path d="m10 1 2.8 6 6.2.6-4.7 4.2 1.4 6.2L10 14.8 4.3 18l1.4-6.2L1 7.6 7.2 7z"/></svg></div>
</div>
<div class="abs quote" style="left:688px;top:2271px">
  <div class="who"><span class="avatar a5" role="img" aria-label="Client portrait"></span>Dominic United States</div>
  <p>I've seen this product grow and develop over the past few years and it keeps getting better! I really like how easy it is to use.</p>
  <div class="stars"><svg viewBox="0 0 20 20"><path d="m10 1 2.8 6 6.2.6-4.7 4.2 1.4 6.2L10 14.8 4.3 18l1.4-6.2L1 7.6 7.2 7z"/></svg><svg viewBox="0 0 20 20"><path d="m10 1 2.8 6 6.2.6-4.7 4.2 1.4 6.2L10 14.8 4.3 18l1.4-6.2L1 7.6 7.2 7z"/></svg><svg viewBox="0 0 20 20"><path d="m10 1 2.8 6 6.2.6-4.7 4.2 1.4 6.2L10 14.8 4.3 18l1.4-6.2L1 7.6 7.2 7z"/></svg><svg viewBox="0 0 20 20"><path d="m10 1 2.8 6 6.2.6-4.7 4.2 1.4 6.2L10 14.8 4.3 18l1.4-6.2L1 7.6 7.2 7z"/></svg><svg viewBox="0 0 20 20"><path d="m10 1 2.8 6 6.2.6-4.7 4.2 1.4 6.2L10 14.8 4.3 18l1.4-6.2L1 7.6 7.2 7z"/></svg></div>
</div>
<div class="abs slider-btn next">›</div>

<!-- contact -->
<svg class="shape" style="top:2585px" width="1200" height="650" viewBox="0 2585 1200 650">
  <defs><radialGradient id="tunnel" cx="50%" cy="40%" r="65%"><stop offset="0" stop-color="#1d4a6b"/><stop offset=".6" stop-color="#0c2238"/><stop offset="1" stop-color="#06121f"/></radialGradient></defs>
  <polygon points="0,2760 872,2597 1200,2696 1200,3231 0,3231" fill="url(#tunnel)"/>
  <polygon points="0,2750 872,2587 1200,2686 1200,2696 872,2597 0,2760" fill="#0a78c2"/>
</svg>
<h2 class="abs contact-title">Contact us for<br>your next Datavane!</h2>
<p class="abs contact-lead">Contact Us And We'll get in touch</p>
<div class="abs reach" style="top:2970px"><span class="ico"><svg viewBox="0 0 24 24"><path d="M4 5h16v10H9l-5 4z"/></svg></span><b>Chat With Us</b></div>
<div class="abs reach" style="top:3037px"><span class="ico"><svg viewBox="0 0 24 24"><rect x="3" y="6" width="18" height="12"/><path d="m3 6 9 7 9-7"/></svg></span><div><small>E-mail us</small><b>hello@datavane.example</b></div></div>
<div class="abs reach" style="top:3102px"><span class="ico"><svg viewBox="0 0 24 24"><path d="M5 3h4l2 5-3 2a11 11 0 0 0 6 6l2-3 5 2v4a2 2 0 0 1-2 2A17 17 0 0 1 3 5a2 2 0 0 1 2-2z"/></svg></span><div><small>Call us</small><b>Tel: +31 20 555 0142</b></div></div>

<div class="abs form-label">Send us a message</div>
<div class="abs field" style="left:611px;top:2849px;width:455px;height:38px">Your Name</div>
<div class="abs field" style="left:611px;top:2898px;width:223px;height:40px">E-Mail</div>
<div class="abs field" style="left:843px;top:2898px;width:223px;height:40px">Phone</div>
<div class="abs field" style="left:611px;top:2950px;width:455px;height:39px">Company</div>
<div class="abs field" style="left:611px;top:3003px;width:455px;height:105px">Type Here</div>
<div class="abs btn submit">Submit Now</div>

<!-- footer -->
<div class="abs brand foot-brand"><span class="mark" style="background:var(--blue)"></span>Datavane</div>
<div class="abs socials" aria-label="Social links"><span></span><span></span><span></span><span></span></div>

<h3 class="abs foot-h" style="left:342px">Quick Links</h3>
<ul class="abs foot-list" style="left:342px;top:3364px;width:160px">
  <li>Home</li><li>Solutions</li><li>Benefits of Choosing Datavane</li><li>Testimonials</li><li>Contact</li>
</ul>

<h3 class="abs foot-h" style="left:553px">Contact</h3>
<ul class="abs foot-list foot-contact" style="left:553px;top:3364px;width:250px">
  <li><svg viewBox="0 0 24 24"><path d="M5 3h4l2 5-3 2a11 11 0 0 0 6 6l2-3 5 2v4a2 2 0 0 1-2 2A17 17 0 0 1 3 5a2 2 0 0 1 2-2z"/></svg>+31 20 555 0142</li>
  <li><svg viewBox="0 0 24 24"><path d="M12 2a7 7 0 0 0-7 7c0 5 7 13 7 13s7-8 7-13a7 7 0 0 0-7-7zm0 10a3 3 0 1 1 0-6 3 3 0 0 1 0 6z"/></svg>48 Harbor Works Ln, Ste. 210, Millbrook, GA, 30599</li>
  <li><svg viewBox="0 0 24 24"><path d="M2 5h20v14H2zm2 2 8 6 8-6"/></svg>hello@datavane.example</li>
</ul>

<h3 class="abs foot-h" style="left:838px">Newsletter</h3>
<div class="abs news">Enter Your Email<svg viewBox="0 0 24 24"><path d="M2 11 22 3l-6 18-4-7z"/></svg></div>

<div class="abs rule"></div>
<p class="abs copy">© Datavane. All Rights Reserved 2025</p>
<svg class="abs chat-fab" viewBox="0 0 42 38" aria-label="Open chat"><path d="M4 4h28a4 4 0 0 1 4 4v16a4 4 0 0 1-4 4H14l-8 7v-7H4a4 4 0 0 1-4-4V8a4 4 0 0 1 4-4z" fill="#0a78c2"/><circle cx="11" cy="16" r="2.5" fill="#fff"/><circle cx="18" cy="16" r="2.5" fill="#fff"/><circle cx="25" cy="16" r="2.5" fill="#fff"/></svg>

</body>
</html>
```